brightfieldhope christian ministry

We need a logo and website design for a contemporary, non-denominational, christian teaching ministry in Australia.

Our audience is christian, 20-45, male and female. The vibe of the ministry is confident, charismatic, energetic, bold, modern yet grounded in biblical truth. Intelligent, humorous, authentic,

Non catholic, not gaudy, not slick, not bland, not overly traditional or liturgical.

We have an emphasis on the Pentecostal phenomena of God the Holy Spirit in dynamic encounter along with reverence for God the Father, God the Son and the Bible.

On the website, we'd like it to be possible for visitors to download audio/video files easily to their devices by clicking on tiles.

we'd like to have a forum for questions. Discussion Board.

we'd like to be able to incorporate bible study software like Lampwell study Guide.
we'd like to be able to have a blog.

we'd like images to be cool and stylised, not cheesy.

A couple of websites I like the look of are: www.cedarmount.example ; rvt.example.au ; www.harbourlightglobal.example ; www.onpath.example although these are much more comprehensive than our start up.

we would like to be able to combine Chirplet and Friendwall with website.

we'd like to be able to edit and upload files easily without too much technical know-how.

at present i don't have content, but am looking for look ideas
Updates

Target Market(s)

25-45 christians

Industry/Entity Type

Christian

Logo Text

BrightFieldHope

Number of Pages Required

5+ page

Requirements
Must have
• impact
• style
• I am not sure what coded/uncoded means, but I am not a techie. I want you to design me a website that I can then use and edit easily.
Nice to have
• arty aesthetic,
• simple, solitary, ability to feed from website to FW and CHIRPLET and put audio files into tunebox
Should not have
• overly catholic imagery
• cliche dove
• not too dreary

```html
<!DOCTYPE html>
<html lang="en">
<head>
<meta charset="utf-8">
<title>BrightFieldHope — Home</title>
<link href="https://fonts.googleapis.com/css2?family=Poppins:wght@300;400;500;600;700&display=swap" rel="stylesheet">
<style>
:root{
  --yellow:#f9c800;
  --navy:#14136b;
  --ink:#2b2b2b;
  --muted:#555;
  --line:#dcdcdc;
  --white:#fff;
  --dark-badge:#3a3a3a;
  --footer:#0e0d2e;
  --night:#07040f;
}
*{margin:0;padding:0;box-sizing:border-box}
html,body{width:1200px;height:3186px;overflow:hidden}
body{position:relative;background:var(--white);font-family:"Poppins",Arial,sans-serif;color:var(--ink)}
.abs{position:absolute}

/* stage-light photo tones */
.tone-violet{background:
  radial-gradient(circle at 22% 18%,rgba(255,255,255,.85) 0,rgba(190,120,255,.6) 8%,transparent 22%),
  radial-gradient(circle at 72% 14%,rgba(255,210,255,.9) 0,rgba(255,80,220,.6) 9%,transparent 24%),
  radial-gradient(ellipse at 50% 45%,#ff3fc8 0,#9a2bd8 30%,transparent 62%),
  linear-gradient(180deg,#2a1fb0 0%,#7a22c8 45%,#3a0b5a 68%,var(--night) 86%)}
.tone-teal{background:
  radial-gradient(circle at 50% 10%,#ffffff 0,#d8fff4 14%,transparent 40%),
  radial-gradient(ellipse at 20% 40%,#2fd6a6 0,transparent 45%),
  linear-gradient(180deg,#b8f2e2 0%,#1f9c78 40%,#0c3a30 70%,#030d0a 100%)}
.tone-smoke{background:
  radial-gradient(circle at 60% 30%,#f0ede4 0,#a8a294 20%,transparent 55%),
  linear-gradient(180deg,#6e6a62 0%,#3a3834 55%,#111 100%)}
.tone-ember{background:
  radial-gradient(circle at 30% 20%,#fff3d6 0,#ff9a50 14%,transparent 36%),
  radial-gradient(circle at 80% 40%,#ff5a2a 0,transparent 35%),
  linear-gradient(160deg,#e86a34 0%,#8a1e10 45%,#2a0604 80%,#0a0202 100%)}
.tone-gold{background:
  radial-gradient(circle at 65% 22%,#ffffff 0,#fff0a0 12%,#ffb400 32%,transparent 60%),
  linear-gradient(180deg,#ffd84a 0%,#f08a00 45%,#5a1c00 75%,#120500 100%)}
.tone-haze{background:
  radial-gradient(circle at 50% 25%,#ffffff 0,#e6e6e6 18%,transparent 48%),
  linear-gradient(180deg,#cfcfcf 0%,#7b7b7b 48%,#262626 75%,#080808 100%)}
.tone-red{background:
  radial-gradient(circle at 30% 12%,#fff 0,#ffb0b0 10%,transparent 28%),
  radial-gradient(circle at 75% 15%,#ffe0a0 0,#ff5a3a 14%,transparent 34%),
  linear-gradient(180deg,#f0a080 0%,#c02a2a 45%,#3a0808 75%,#0a0202 100%)}
.tone-blue{background:
  radial-gradient(circle at 30% 20%,#aaf0ff 0,#2ad0ff 12%,transparent 32%),
  radial-gradient(circle at 75% 25%,#3aff7a 0,transparent 26%),
  radial-gradient(circle at 55% 10%,#ff3a6a 0,transparent 20%),
  linear-gradient(180deg,#2a5af0 0%,#1a2a9a 45%,#070826 80%,#020208 100%)}
.tone-pink{background:
  radial-gradient(circle at 25% 15%,#fff 0,#ffb8f4 10%,transparent 28%),
  radial-gradient(circle at 78% 18%,#fff 0,#ff7ae0 12%,transparent 30%),
  linear-gradient(180deg,#f0b0f0 0%,#c23ad0 40%,#3a0848 72%,#080210 100%)}
.tone-heart{background:
  radial-gradient(circle at 40% 30%,#fff 0,#c8a8ff 10%,transparent 30%),
  radial-gradient(circle at 80% 60%,#ff4ad8 0,transparent 40%),
  linear-gradient(135deg,#2a3bd0 0%,#8a3ae0 40%,#3a1060 70%,#0a0418 100%)}
.tone-stage{background:
  radial-gradient(circle at 50% 22%,#fff8d0 0,#ffd060 14%,transparent 36%),
  radial-gradient(circle at 50% 90%,#ff9a1a 0,transparent 40%),
  linear-gradient(180deg,#c85a10 0%,#6a2208 45%,#2a0a04 75%,#a04a08 100%)}
.tone-worship{background:
  radial-gradient(circle at 50% 45%,#ffffff 0,#f2d8ee 16%,#b05a9c 40%,transparent 70%),
  radial-gradient(circle at 15% 20%,#ff8ad8 0,transparent 30%),
  linear-gradient(180deg,#4a1838 0%,#1a0810 70%,#050203 100%)}

/* hero */
.hero{left:0;top:0;width:1200px;height:563px;background:
  radial-gradient(circle at 18% 30%,rgba(255,255,255,.7) 0,rgba(170,120,255,.5) 6%,transparent 18%),
  radial-gradient(circle at 82% 26%,rgba(255,255,255,.7) 0,rgba(255,110,230,.55) 6%,transparent 18%),
  radial-gradient(ellipse at 50% 58%,#ff5ad0 0,#c43ad8 22%,#6a2ac8 45%,transparent 70%),
  linear-gradient(180deg,#1a17a8 0%,#3424b8 35%,#7a2ab8 58%,#2a0c48 78%,var(--night) 92%)}
.brand{left:161px;top:40px;display:flex;align-items:center;gap:10px}
.brand-mark{width:30px;height:30px;border-radius:50%;background:var(--yellow)}
.brand-name{font-size:14px;font-weight:600;color:var(--white)}
.nav{left:321px;top:49px;display:flex;gap:19px;font-size:12.5px;font-weight:500;color:var(--white)}
.nav .active{color:var(--yellow);border-bottom:2px solid var(--yellow);padding-bottom:5px}
.play{fill:none;stroke:var(--white);stroke-width:2.5}
.play-gold{fill:none;stroke:var(--yellow);stroke-width:2.5}

.section-title{width:1200px;left:0;text-align:center;font-size:21px;font-weight:600;color:var(--ink)}

/* about */
.about-media{left:161px;top:622px;width:427px;height:266px}
.about-title{left:665px;top:676px;font-size:21px;font-weight:600}
.about-text{left:665px;top:723px;width:375px;font-size:11.5px;line-height:18.5px;color:var(--muted)}

/* ministry tiles */
.tile{top:949px;width:400px;height:289px;display:flex;align-items:center;justify-content:center}
.tile-channel{left:0}
.tile-ministries{left:400px;border-left:2px solid var(--white);border-right:2px solid var(--white)}
.tile-music{left:800px}
.tile-label{font-size:22px;font-weight:400;color:var(--white)}
.tile-box{width:238px;height:123px;background:rgba(40,40,40,.72);display:flex;align-items:center;justify-content:center}
.tile-box.gold .tile-label{color:var(--yellow)}

/* events */
.event{top:1344px;width:202px}
.event-media{width:202px;height:142px;position:relative}
.date{position:absolute;left:0;top:0;width:46px;height:46px;background:var(--dark-badge);color:var(--white);font-size:11px;line-height:14px;display:flex;flex-direction:column;justify-content:center;padding-left:10px}
.date.gold{background:var(--yellow)}
.event-caption{margin-top:14px;font-size:10px;color:var(--muted)}
.btn-fill{background:var(--yellow);color:var(--white);font-size:11px;display:flex;align-items:center;justify-content:center}
.btn-line{border:2px solid var(--yellow);color:var(--yellow);font-size:11px;display:flex;align-items:center;justify-content:center}

/* collection */
.collection{left:0;top:1684px;width:1200px;height:317px;display:grid;grid-template-columns:repeat(5,240px);grid-template-rows:repeat(2,158.5px)}
.media-tile{position:relative;display:flex;align-items:center;justify-content:center}
.download{position:absolute;right:14px;top:10px}

/* blog */
.post{top:2181px;width:285px}
.post-media{width:285px;height:209px}
.post-bar{display:flex;height:50px;background:#f3f3f3}
.post-bar .date{position:static;width:48px;height:50px}
.post-title{flex:1;display:flex;align-items:center;padding-left:12px;font-size:13.5px;font-weight:500;color:var(--ink)}

/* contact + board */
.contact{left:161px;top:2568px;width:451px;height:452px;background:var(--yellow);padding:32px 24px}
.contact h3{font-size:21px;font-weight:600;color:var(--white);margin-bottom:20px}
.field{background:var(--white);height:33px;margin-bottom:12px;font-size:10.5px;color:#b0b0b0;padding:8px 10px}
.field.message{height:143px;margin-bottom:18px}
.send{width:120px;height:38px;border:2px solid var(--white);color:var(--white);font-size:11px;display:flex;align-items:center;justify-content:center}
.board{left:635px;top:2568px;width:404px;height:452px;border:2px solid var(--line);padding:32px 23px}
.board h3{font-size:21px;font-weight:600;margin-bottom:18px}
.topic{height:37px;border:1px solid var(--line);margin-bottom:-1px;display:flex;justify-content:space-between;align-items:center;padding:0 10px;font-size:11px;color:#9a9a9a}
.topic span:last-child{font-size:16px;color:#aaa}

/* footer */
.footer{left:0;top:3080px;width:1200px;height:106px;background:linear-gradient(180deg,var(--footer),#05040f)}
.footer-links{left:161px;top:3120px;font-size:10px;color:var(--white)}
.footer-copy{left:161px;top:3136px;font-size:10px;color:var(--white)}
.social{top:3112px;width:44px;height:44px;border-radius:50%;display:flex;align-items:center;justify-content:center;font-size:11px;font-weight:600}
.social.fw{left:943px;background:var(--white);color:var(--footer)}
.social.ch{left:995px;background:#1da1f2;color:var(--white)}
</style>
</head>
<body>

<div class="abs hero" role="img" aria-label="Concert crowd with raised hands under purple and pink stage lights"></div>
<div class="abs brand"><span class="brand-mark"></span><span class="brand-name">BrightFieldHope</span></div>
<nav class="abs nav">
  <span class="active">HOME</span><span>ABOUT US</span><span>CHANNEL</span><span>MINISTRIES</span><span>MUSIC</span><span>EVENTS</span><span>STORE</span><span>BLOG</span><span>FAQ</span><span>CONTACT US</span>
</nav>
<svg class="abs" style="left:567px;top:248px" width="64" height="64" viewBox="0 0 64 64"><circle class="play" cx="32" cy="32" r="30"/><path class="play" d="M26 20 L44 32 L26 44 Z"/></svg>

<div class="abs about-media tone-worship" role="img" aria-label="Worshipper with raised arms against bright stage light"></div>
<svg class="abs" style="left:343px;top:724px" width="64" height="64" viewBox="0 0 64 64"><circle class="play" cx="32" cy="32" r="30"/><path class="play" d="M26 20 L44 32 L26 44 Z"/></svg>
<h2 class="abs about-title">About Us</h2>
<p class="abs about-text">Lorem ipsum dolor sit amet, consectetur adipiscing elit. Ut placerat vitae leo eget vestibulum. Morbi tortor orci, tempus vitae felis ut, luctus imperdiet nulla. Aliquam pellentesque cursus elit condimentum porttitor. Nam feugiat nisi risus, sed pharetra dolor consectetur quis. Donec eu purus augue. Interdum et malesuada fames ac ante ipsum primis in faucibus.</p>

<div class="abs tile tile-channel tone-heart" role="img" aria-label="Hands forming a heart against blue and purple light"><span class="tile-label">CHANNEL</span></div>
<div class="abs tile tile-ministries tone-stage" role="img" aria-label="Stage with warm golden lights over a crowd"><div class="tile-box gold"><span class="tile-label">MINISTRIES</span></div></div>
<div class="abs tile tile-music tone-pink" role="img" aria-label="Crowd with raised hands under pink stage lights"><div class="tile-box"><span class="tile-label">MUSIC</span></div></div>

<h2 class="abs section-title" style="top:1290px">Latest Events</h2>
<div class="abs event" style="left:161px"><div class="event-media tone-haze" role="img" aria-label="Concert crowd in white haze"><div class="date">24<span>Jan</span></div></div><p class="event-caption">Lorem ipsum dolor sit amet</p></div>
<div class="abs event" style="left:387px"><div class="event-media tone-red" role="img" aria-label="Red stage lights over a festival crowd"><div class="date gold">25<span>Jan</span></div></div><p class="event-caption">Lorem ipsum dolor sit amet</p></div>
<div class="abs event" style="left:612px"><div class="event-media tone-violet" role="img" aria-label="Purple and blue stage lights over a crowd"><div class="date">26<span>Jan</span></div></div><p class="event-caption">Lorem ipsum dolor sit amet</p></div>
<div class="abs event" style="left:837px"><div class="event-media tone-gold" role="img" aria-label="Yellow stage glow over a concert crowd"><div class="date">27<span>Jan</span></div></div><p class="event-caption">Lorem ipsum dolor sit amet</p></div>
<div class="abs btn-fill" style="left:540px;top:1540px;width:121px;height:36px">Load More</div>

<h2 class="abs section-title" style="top:1632px">Our Collection</h2>
<div class="abs collection">
  <div class="media-tile tone-violet" role="img" aria-label="Pink stage lights over a crowd"><svg width="50" height="50" viewBox="0 0 64 64"><circle class="play" cx="32" cy="32" r="30"/><path class="play" d="M26 20 L44 32 L26 44 Z"/></svg><svg class="download" width="20" height="20" viewBox="0 0 20 20"><path d="M10 2v11M5 8l5 5 5-5M3 17h14" stroke="#fff" stroke-width="2.5" fill="none"/></svg></div>
  <div class="media-tile tone-teal" role="img" aria-label="Crowd under green and teal light"></div>
  <div class="media-tile tone-smoke" role="img" aria-label="Worshipper with arms raised in a dim hall"><svg width="50" height="50" viewBox="0 0 64 64"><circle class="play-gold" cx="32" cy="32" r="30"/><path class="play-gold" d="M26 20 L44 32 L26 44 Z"/></svg><svg class="download" width="20" height="20" viewBox="0 0 20 20"><path d="M10 2v11M5 8l5 5 5-5M3 17h14" stroke="#f9c800" stroke-width="2.5" fill="none"/></svg></div>
  <div class="media-tile tone-ember" role="img" aria-label="Guitar strings in warm red light"><svg width="50" height="50" viewBox="0 0 64 64"><circle class="play" cx="32" cy="32" r="30"/><path class="play" d="M26 20 L44 32 L26 44 Z"/></svg><svg class="download" width="20" height="20" viewBox="0 0 20 20"><path d="M10 2v11M5 8l5 5 5-5M3 17h14" stroke="#fff" stroke-width="2.5" fill="none"/></svg></div>
  <div class="media-tile tone-gold" role="img" aria-label="Raised hands against golden light"><svg class="download" width="20" height="20" viewBox="0 0 20 20"><path d="M10 2v11M5 8l5 5 5-5M3 17h14" stroke="#fff" stroke-width="2.5" fill="none"/></svg></div>
  <div class="media-tile tone-violet" role="img" aria-label="Pink stage lights over a crowd"><svg width="50" height="50" viewBox="0 0 64 64"><circle class="play" cx="32" cy="32" r="30"/><path class="play" d="M26 20 L44 32 L26 44 Z"/></svg><svg class="download" width="20" height="20" viewBox="0 0 20 20"><path d="M10 2v11M5 8l5 5 5-5M3 17h14" stroke="#fff" stroke-width="2.5" fill="none"/></svg></div>
  <div class="media-tile tone-teal" role="img" aria-label="Crowd under green and teal light"><svg class="download" width="20" height="20" viewBox="0 0 20 20"><path d="M10 2v11M5 8l5 5 5-5M3 17h14" stroke="#fff" stroke-width="2.5" fill="none"/></svg></div>
  <div class="media-tile tone-smoke" role="img" aria-label="Worshipper among a bright crowd"><svg width="50" height="50" viewBox="0 0 64 64"><circle class="play" cx="32" cy="32" r="30"/><path class="play" d="M26 20 L44 32 L26 44 Z"/></svg></div>
  <div class="media-tile tone-ember" role="img" aria-label="Guitar strings in warm red light"><svg width="50" height="50" viewBox="0 0 64 64"><circle class="play" cx="32" cy="32" r="30"/><path class="play" d="M26 20 L44 32 L26 44 Z"/></svg></div>
  <div class="media-tile tone-gold" role="img" aria-label="Raised hands against golden light"></div>
</div>
<div class="abs btn-line" style="left:540px;top:2033px;width:121px;height:36px">View More</div>

<h2 class="abs section-title" style="top:2123px">Our Blog</h2>
<div class="abs post" style="left:161px"><div class="post-media tone-blue" role="img" aria-label="Blue and green lights over a cheering crowd"></div><div class="post-bar"><div class="date">28<span>Jan</span></div><div class="post-title">Lorem ipsum dolor sit amet.</div></div></div>
<div class="abs post" style="left:459px"><div class="post-media tone-gold" role="img" aria-label="Golden stage glow over raised fists"></div><div class="post-bar"><div class="date gold">29<span>Jan</span></div><div class="post-title">Lorem ipsum dolor sit amet.</div></div></div>
<div class="abs post" style="left:756px"><div class="post-media tone-pink" role="img" aria-label="Raised hands under pink stage lights"></div><div class="post-bar"><div class="date">30<span>Jan</span></div><div class="post-title">Lorem ipsum dolor sit amet.</div></div></div>
<div class="abs btn-line" style="left:540px;top:2470px;width:121px;height:36px">View More</div>

<section class="abs contact">
  <h3>Contact Us</h3>
  <div class="field">Name</div>
  <div class="field">Email address</div>
  <div class="field message">Message</div>
  <div class="send">Send Now</div>
</section>
<section class="abs board">
  <h3>Discussion Board</h3>
  <div class="topic"><span>Lorem ipsum dolor sit amet...</span><span>+</span></div>
  <div class="topic"><span>Lorem ipsum dolor sit amet...</span><span>+</span></div>
  <div class="topic"><span>Lorem ipsum dolor sit amet...</span><span>+</span></div>
  <div class="topic"><span>Lorem ipsum dolor sit amet...</span><span>+</span></div>
  <div class="topic"><span>Lorem ipsum dolor sit amet...</span><span>+</span></div>
  <div class="topic"><span>Lorem ipsum dolor sit amet...</span><span>+</span></div>
  <div class="topic"><span>Lorem ipsum dolor sit amet...</span><span>+</span></div>
  <div class="topic"><span>Lorem ipsum dolor sit amet...</span><span>+</span></div>
</section>

<footer class="abs footer"></footer>
<div class="abs footer-links">HOME &nbsp;|&nbsp; ABOUT US &nbsp;|&nbsp; CHANNEL &nbsp;|&nbsp; MINISTRIES &nbsp;|&nbsp; MUSIC &nbsp;|&nbsp; EVENTS &nbsp;|&nbsp; STORE &nbsp;|&nbsp; BLOG &nbsp;|&nbsp; FAQ &nbsp;|&nbsp; CONTACT US</div>
<div class="abs footer-copy">Copyright © 2017 BrightFieldHope. All Rights Reserved.</div>
<div class="abs social fw" aria-label="Friendwall">FW</div>
<div class="abs social ch" aria-label="Chirplet">CH</div>

</body>
</html>
```